Varnath Consulting Business card design.

See our website www.varnathconsulting-example.com which will give you a good idea of what we are about. The font is called 'Play'.

I'd like a standout business card in keeping with the themes and branding on the website

Target Market(s)

professionals. HR directors

Industry/Entity Type

Business

Contact Information for Business Card

Varnath Consulting PO Box 3917 Tindale Creek NSW 2840 1300 457 318 Gerald Ashbury Principal email: jobs@varnathconsulting-example.com ABN: 31792048663

Font styles to use
Other font styles liked:
• Play

Requirements
Must have
• Must have same design colours and branding as website.
• On back I'd prefer a list of the things we do which appears below the name at the header on the website

```html
<!DOCTYPE html>
<html lang="en">
<head>
<meta charset="utf-8">
<title>Varnath Consulting – Business Card</title>
<link rel="stylesheet" href="https://fonts.googleapis.com/css2?family=Play:wght@400;700&display=swap">
<style>
  :root {
    --board: #808080;
    --navy: #0d1f30;
    --sky-top: #2f6ec4;
    --sky-mid: #4d8fd8;
    --snow: #c9d9ee;
    --wave: #dfe3e1;
    --white: #ffffff;
    --accent: #3b8fd1;
    --shadow: rgba(0, 0, 0, 0.55);
  }
  * { margin: 0; padding: 0; box-sizing: border-box; }
  html, body {
    width: 992px; height: 1200px; overflow: hidden;
    background: var(--board);
    font-family: 'Play', sans-serif;
    color: var(--white);
  }
  .board { position: relative; width: 992px; height: 1200px; }
  .card {
    position: absolute; left: 67px; width: 862px; height: 491px;
    background: var(--navy);
    box-shadow: 8px 10px 10px var(--shadow);
    overflow: hidden;
  }
  .card--front { top: 66px; }
  .card--back { top: 621px; }
  .front-art { position: absolute; inset: 0; }
  .brand {
    position: absolute; left: 40px; top: 78px;
    font-size: 44px; font-weight: 400; letter-spacing: 1px; line-height: 1;
  }
  .services {
    position: absolute; left: 40px; top: 140px;
    font-size: 13px; letter-spacing: 1.6px; line-height: 1; white-space: nowrap;
  }
  .person { position: absolute; right: 30px; top: 286px; text-align: right; }
  .person__name { font-size: 28px; font-weight: 700; letter-spacing: 0.5px; line-height: 1.05; }
  .person__role { font-size: 21px; line-height: 1.3; }
  .contacts { position: absolute; right: 22px; top: 380px; list-style: none; }
  .contacts li {
    display: flex; justify-content: flex-end; align-items: center;
    height: 32px; font-size: 20px; letter-spacing: 0.3px;
  }
  .contacts svg { width: 22px; height: 22px; margin-left: 22px; fill: var(--white); }
  .abn { position: absolute; left: 34px; top: 444px; font-size: 20px; letter-spacing: 0.3px; }
  .back-brand {
    position: absolute; left: 0; right: 0; top: 190px; text-align: center;
    font-size: 55px; letter-spacing: 2px; line-height: 1;
  }
  .back-services {
    position: absolute; left: 0; right: 0; top: 273px; text-align: center;
    font-size: 17px; letter-spacing: 2.2px; color: var(--accent); white-space: nowrap;
  }
</style>
</head>
<body>
<main class="board">
  <section class="card card--front">
    <svg class="front-art" viewBox="0 0 862 491" width="862" height="491">
      <defs>
        <linearGradient id="sky" x1="0" y1="0" x2="0.3" y2="1">
          <stop offset="0" stop-color="var(--sky-top)"/>
          <stop offset="0.6" stop-color="var(--sky-mid)"/>
          <stop offset="1" stop-color="var(--snow)"/>
        </linearGradient>
      </defs>
      <path class="wave" fill="var(--wave)"
        d="M0,205 C60,318 160,392 300,386 C560,380 700,182 862,172 V150 H0 Z"/>
      <path class="photo" role="img" aria-label="Photo of a snowboarder jumping against a blue sky above a snowy mountain peak"
        fill="url(#sky)"
        d="M0,0 H862 V160 C700,168 560,372 296,374 C160,375 60,300 0,205 Z"/>
    </svg>

    <h1 class="brand">VARNATH CONSULTING</h1>
    <p class="services">Search &amp; Select I Career I Coaching I Leadership I Outplacement</p>

    <div class="person">
      <p class="person__name">Gerald Ashbury</p>
      <p class="person__role">Principal</p>
    </div>

    <ul class="contacts">
      <li>1300 457 318
        <svg viewBox="0 0 24 24" aria-hidden="true"><path d="M3 9c0-3 4-5 9-5s9 2 9 5v2h-5V9c-1-.6-2.4-1-4-1s-3 .4-4 1v2H3z M7 12h10l2 7H5z M12 13.5a2 2 0 1 0 0 4a2 2 0 1 0 0-4z" fill-rule="evenodd"/></svg>
      </li>
      <li>jobs@varnathconsulting-example.com
        <svg viewBox="0 0 24 24" aria-hidden="true"><path d="M2 6h20v12H2z M3.5 7.5 12 13.5 20.5 7.5" stroke="var(--navy)" stroke-width="1.4"/></svg>
      </li>
      <li>PO Box 3917 Tindale Creek NSW 2840
        <svg viewBox="0 0 24 24" aria-hidden="true"><path d="M12 2a7 7 0 0 0-7 7c0 5 7 13 7 13s7-8 7-13a7 7 0 0 0-7-7zm0 4a3 3 0 1 1 0 6a3 3 0 1 1 0-6z" fill-rule="evenodd"/></svg>
      </li>
    </ul>

    <p class="abn">ABN: 31792048663</p>
  </section>

  <section class="card card--back">
    <h2 class="back-brand">VARNATH CONSULTING</h2>
    <p class="back-services">Search &amp; Select&nbsp; I &nbsp;Career&nbsp; I &nbsp;Coaching&nbsp; I &nbsp;Leadership&nbsp; I &nbsp;Outplacement</p>
  </section>
</main>
</body>
</html>
```